Trendy Interior Design Company Postcard

We're looking to create a 4x6 or 5x7 double sided postcard type of flyer with our Logo on the front and some photos and information on the back. We would like it to capture peoples attention and to communicate that we are a trendy interior design/build company that can take on a diverse variety of projects to suit any type of client.
We have many more photos of projects, if needed.

Target Market(s)

High end residential home renovations and builds.

Industry/Entity Type

It Company

Font styles to use
Serif
Sans Serif

Requirements
Must have
• Our logo on the front, and on the back we want a variety of photos of our jobs, We would like our company contact information: 555-238-9047 - info@quorvel.ca and something to entice potential clients to contact us, such as " Call for your quote today"
Nice to have
• Diversity in designs. As many photos as possible without looking too busy. We want it to look clean, sleek, and neat. Colours should match our website and logo.
Should not have
• Too much colour. No tacky/unprofessional looking fonts.

```html
<!DOCTYPE html>
<html lang="en">
<head>
<meta charset="utf-8">
<title>Quorvel Homes Inc – Postcard</title>
<link rel="stylesheet" href="https://fonts.googleapis.com/css2?family=Cinzel:wght@400&family=Crimson+Text:wght@400;600;700&display=swap">
<style>
  :root {
    --backdrop: #7b5229;
    --ink: #1b1c1e;
    --panel: #232427;
    --panel-soft: #34353a;
    --silver: #d6d6d6;
    --strip: #d3d3d3;
    --white: #ffffff;
    --band: #d0d0d0;
    --serif-title: "Cinzel", serif;
    --serif-body: "Crimson Text", serif;
  }
  * { box-sizing: border-box; margin: 0; padding: 0; }
  html, body { width: 907px; height: 1200px; overflow: hidden; }
  body { background: var(--backdrop); position: relative; font-family: var(--serif-body); }

  .card { position: absolute; left: 97px; width: 710px; background: var(--strip); box-shadow: 0 4px 14px rgba(0,0,0,.4); overflow: hidden; }

  /* Front */
  .card--front { top: 45px; height: 505px; }
  .front-face { position: absolute; inset: 0 0 55px 0; background: radial-gradient(ellipse at 50% 30%, #3e3f44 0%, #26272a 45%, var(--ink) 80%); }
  .frame-line { position: absolute; background: var(--white); }
  .frame-line--top { left: 0; right: 0; top: 22px; height: 2px; }
  .frame-line--bottom { left: 0; right: 0; bottom: 8px; height: 2px; }
  .frame-line--left { top: 0; bottom: 0; left: 23px; width: 2px; }
  .frame-line--right { top: 0; bottom: 0; right: 27px; width: 2px; }
  .brand { position: absolute; left: 0; right: 0; top: 105px; display: flex; flex-direction: column; align-items: center; }
  .brand-mark { width: 190px; height: 155px; border: 5px solid var(--silver); }
  .brand-name { font-family: var(--serif-title); color: var(--silver); font-size: 42px; letter-spacing: 2px; margin-top: 26px; line-height: 1; }
  .brand-suffix { display: flex; align-items: center; gap: 14px; margin-top: 8px; font-family: var(--serif-title); color: var(--silver); font-size: 18px; letter-spacing: 4px; }
  .brand-suffix::before, .brand-suffix::after { content: ""; width: 155px; height: 2px; background: var(--silver); }
  .web { position: absolute; left: 0; right: 0; bottom: 0; height: 55px; display: flex; align-items: center; justify-content: center;
         font-family: var(--serif-body); font-weight: 700; font-size: 21px; letter-spacing: 8px; color: var(--ink); }

  /* Back */
  .card--back { top: 600px; height: 540px; }
  .photo { position: absolute; }
  .photo--top-sliver { left: 0; top: 0; width: 710px; height: 30px; background: linear-gradient(90deg, #6b5236, #efe9e1 25%, #d7d3ce 60%, #9d9a96); }
  .photo--living { left: 0; top: 30px; width: 222px; height: 152px;
    background:
      linear-gradient(180deg, rgba(0,0,0,0) 60%, rgba(150,85,35,.95) 78%, #8a4e22 100%),
      linear-gradient(90deg, #ecebe8 0%, #c9c2b8 35%, #4c4540 60%, #d9d5cf 80%, #f2f1ee 100%); }
  .photo--bath { left: 0; top: 184px; width: 222px; height: 150px;
    background:
      linear-gradient(180deg, rgba(0,0,0,0) 55%, rgba(45,32,28,.95) 72%, #c9c4bd 88%, #e8e6e2 100%),
      linear-gradient(90deg, #6f655d 0%, #cfc8be 30%, #f2efe9 45%, #9d9388 70%, #5e544d 100%); }
  .photo--kitchen { left: 0; top: 336px; width: 222px; height: 149px;
    background:
      linear-gradient(180deg, rgba(0,0,0,0) 62%, rgba(32,28,27,.9) 80%, #8b8076 100%),
      linear-gradient(90deg, #f4f4f3 0%, #dedede 35%, #6f6a66 55%, #e9e9e7 75%, #b9b9b9 100%); }
  .photo--dining { left: 443px; top: 32px; width: 267px; height: 198px;
    background:
      linear-gradient(180deg, rgba(0,0,0,0) 50%, rgba(40,40,44,.9) 75%, #6f6f72 100%),
      linear-gradient(90deg, #7a7b7f 0%, #d8d8d6 30%, #a9aaad 55%, #eeeeec 80%, #bdbdbd 100%); }
  .photo--modern { left: 443px; top: 322px; width: 267px; height: 163px;
    background:
      linear-gradient(180deg, rgba(0,0,0,0) 55%, rgba(30,29,30,.95) 80%, #2b2a2a 100%),
      linear-gradient(90deg, #4a4644 0%, #d9d6d1 25%, #8e8a86 45%, #e8e6e2 70%, #6d6965 100%); }

  .compare { position: absolute; left: 443px; top: 230px; width: 267px; height: 92px; background: var(--ink); }
  .compare-item { position: absolute; top: 2px; width: 110px; height: 88px; border: 3px solid var(--white); background: var(--white); }
  .compare-item--before { left: 17px; }
  .compare-item--after { left: 145px; }
  .compare-shot { height: 68px; }
  .compare-item--before .compare-shot { background: linear-gradient(180deg, #d9e0e6 0%, #f3f1ee 40%, #3b332e 70%, #7b8a5c 100%); }
  .compare-item--after .compare-shot { background: linear-gradient(180deg, #6f8a55 0%, #8a9a86 40%, #6b7466 70%, #5c7045 100%); }
  .compare-label { height: 14px; background: #3a3a3a; color: var(--white); font-size: 11px; font-weight: 600; text-align: center; line-height: 14px; letter-spacing: .5px; }

  .center-panel { position: absolute; left: 225px; top: 20px; width: 215px; height: 465px; background: linear-gradient(180deg, var(--panel-soft), var(--panel) 60%, var(--ink)); }
  .center-brand { position: absolute; left: 0; right: 0; top: 52px; display: flex; flex-direction: column; align-items: center; }
  .center-brand .brand-mark { width: 140px; height: 95px; border-width: 4px; }
  .center-brand .brand-name { font-size: 19px; letter-spacing: 1px; margin-top: 14px; }
  .cta { position: absolute; left: 0; right: 0; top: 205px; text-align: center; color: var(--white); font-size: 19px; font-weight: 600; line-height: 1.3; }
  .phone-band { position: absolute; left: 0; right: 0; top: 292px; height: 54px; background: var(--band);
                display: flex; align-items: center; justify-content: center; font-size: 27px; font-weight: 700; color: var(--ink); }
  .email { position: absolute; left: 0; right: 0; top: 394px; text-align: center; color: var(--white); font-size: 16px; font-weight: 600; }

  .base-rule { position: absolute; left: 0; right: 0; top: 485px; height: 3px; background: var(--ink); }
</style>
</head>
<body>

<section class="card card--front" aria-label="Postcard front">
  <div class="front-face">
    <div class="frame-line frame-line--top"></div>
    <div class="frame-line frame-line--bottom"></div>
    <div class="frame-line frame-line--left"></div>
    <div class="frame-line frame-line--right"></div>
    <div class="brand">
      <div class="brand-mark"></div>
      <div class="brand-name">QUORVEL HOMES</div>
      <div class="brand-suffix">INC</div>
    </div>
  </div>
  <div class="web">www.quorvel.ca</div>
</section>

<section class="card card--back" aria-label="Postcard back">
  <div class="photo photo--top-sliver" role="img" aria-label="Edge of another project photo"></div>
  <div class="photo photo--living" role="img" aria-label="Living room with wood shelving, wall-mounted television and warm wood floor"></div>
  <div class="photo photo--bath" role="img" aria-label="Modern bathroom with glass shower and dark vanity"></div>
  <div class="photo photo--kitchen" role="img" aria-label="White kitchen with island and bar stools"></div>

  <div class="center-panel">
    <div class="center-brand">
      <div class="brand-mark"></div>
      <div class="brand-name">QUORVEL HOMES</div>
    </div>
    <p class="cta">CALL FOR<br>YOUR QUOTE<br>TODAY</p>
    <div class="phone-band">555-238-9047</div>
    <p class="email">info@quorvel.ca</p>
  </div>

  <div class="photo photo--dining" role="img" aria-label="Open kitchen and dining area with pendant lights"></div>
  <div class="compare">
    <div class="compare-item compare-item--before">
      <div class="compare-shot" role="img" aria-label="House exterior before renovation"></div>
      <div class="compare-label">BEFORE</div>
    </div>
    <div class="compare-item compare-item--after">
      <div class="compare-shot" role="img" aria-label="House exterior after renovation"></div>
      <div class="compare-label">AFTER</div>
    </div>
  </div>
  <div class="photo photo--modern" role="img" aria-label="Contemporary kitchen with marble and stainless finishes"></div>

  <div class="base-rule"></div>
  <div class="web">www.quorvel.ca</div>
</section>

</body>
</html>
```